Digital Billboard Design: Winter Sales Event

I own a boutique furniture store in Calgary, AB (maplewoven.ca) and I am looking to advertise our winter sale event on a new curved digital billboard (specs attached including required file type).

I have this billboard rented for 52-weeks so I will be looking to change the design every 4-weeks (i.e. this is intended to be an ongoing project).

The objective of this first billboard is to raise awareness around our annual winter sales event. The store itself is only a few blocks from the billboard so those commuting into downtown are just a short drive from the store.

I am looking for a fresh, clean, contemporary look that will grab your attention as you drive into downtown Calgary without presenting to much info so as to be distracting (and overwhelming -- the billboard does not need to contain all info on my current marketing material). I should also note that the store caters to a higher-end, more sophisticated clientele so the graphics need to reflect the brand (i.e. we are not Brenton Furniture or Couch Depot!).

I have attached three files:

Billboard specs
Current marketing material advertising sale (and all relevant data)
An idea that is from an American furniture store that I think is interesting

Target Market(s)

Upper middle class, sophisticated client who appreciates the finer things in life.

Industry/Entity Type

Furniture Store

Font styles to use
Sans Serif

Requirements
Must have
• Company Logo
• Winter Sales Event - 20 to 60% off
• Address: 3847 22nd Ave SW
Nice to have
• Image of furniture -- see our website www.maplewoven.ca -- any photo from this site can be used
Should not have
• Too much text or visual distration

```html
<!DOCTYPE html>
<html lang="en">
<head>
<meta charset="utf-8">
<title>Winter Sales Event Billboard</title>
<link rel="stylesheet" href="https://fonts.googleapis.com/css2?family=Arimo:wght@400;700&family=Montserrat:wght@300&display=swap">
<style>
  :root {
    --stage: #1e1e1e;
    --sky-light: #2aaae6;
    --sky-mid: #1f96da;
    --sky-edge: #1577c6;
    --snow: #ffffff;
    --frost: rgba(235, 244, 255, 0.75);
    --frost-fade: rgba(235, 244, 255, 0);
  }
  * { margin: 0; padding: 0; box-sizing: border-box; }
  html, body {
    width: 1200px;
    height: 1000px;
    overflow: hidden;
    background: var(--stage);
  }
  .billboard {
    position: absolute;
    left: 163px;
    top: 237px;
    width: 894px;
    height: 415px;
    overflow: hidden;
    background: radial-gradient(ellipse 60% 70% at 50% 55%, var(--sky-light) 0%, var(--sky-mid) 55%, var(--sky-edge) 100%);
    color: var(--snow);
    font-family: "Arimo", Arial, sans-serif;
    text-align: center;
  }
  .snowfall {
    position: absolute;
    top: 0;
    height: 100%;
  }
  .snowfall--left {
    left: 0;
    width: 110px;
    background:
      radial-gradient(circle 42px at 42px 53px, var(--frost), var(--frost-fade)),
      radial-gradient(circle 28px at 96px 12px, var(--frost), var(--frost-fade)),
      radial-gradient(circle 26px at 18px 128px, var(--frost), var(--frost-fade)),
      radial-gradient(circle 34px at 72px 173px, var(--frost), var(--frost-fade)),
      radial-gradient(circle 16px at 10px 198px, var(--frost), var(--frost-fade)),
      radial-gradient(circle 46px at 54px 275px, var(--frost), var(--frost-fade)),
      radial-gradient(circle 30px at 26px 360px, var(--frost), var(--frost-fade)),
      radial-gradient(circle 24px at 77px 398px, var(--frost), var(--frost-fade));
  }
  .snowfall--right {
    right: 0;
    width: 150px;
    background:
      radial-gradient(circle 32px at 30px 18px, var(--frost), var(--frost-fade)),
      radial-gradient(circle 42px at 98px 53px, var(--frost), var(--frost-fade)),
      radial-gradient(circle 18px at 95px 125px, var(--frost), var(--frost-fade)),
      radial-gradient(circle 32px at 130px 171px, var(--frost), var(--frost-fade)),
      radial-gradient(circle 24px at 61px 213px, var(--frost), var(--frost-fade)),
      radial-gradient(circle 30px at 116px 268px, var(--frost), var(--frost-fade)),
      radial-gradient(circle 28px at 88px 328px, var(--frost), var(--frost-fade)),
      radial-gradient(circle 32px at 60px 388px, var(--frost), var(--frost-fade)),
      radial-gradient(circle 20px at 125px 383px, var(--frost), var(--frost-fade));
  }
  .headline {
    position: absolute;
    left: 0;
    right: 0;
    top: 16px;
    font-size: 58px;
    font-weight: 700;
    line-height: 1;
  }
  .headline-rule {
    position: absolute;
    left: 150px;
    width: 584px;
    top: 77px;
    height: 2px;
    background: var(--snow);
  }
  .discount {
    position: absolute;
    left: 0;
    right: 0;
    top: 91px;
    font-size: 40px;
    font-weight: 400;
    line-height: 1;
  }
  .brand-mark {
    position: absolute;
    left: 397px;
    top: 158px;
    width: 100px;
    height: 100px;
    background: var(--snow);
  }
  .brand-name {
    position: absolute;
    left: 0;
    right: 0;
    top: 289px;
    font-family: "Montserrat", Arial, sans-serif;
    font-weight: 300;
    font-size: 58px;
    letter-spacing: 10px;
    line-height: 1;
  }
  .address {
    position: absolute;
    left: 0;
    right: 0;
    top: 367px;
    font-size: 35px;
    font-weight: 400;
    line-height: 1;
  }
</style>
</head>
<body>
  <section class="billboard">
    <div class="snowfall snowfall--left" role="img" aria-label="Scattered white snowflakes along the left edge"></div>
    <div class="snowfall snowfall--right" role="img" aria-label="Scattered white snowflakes along the right edge"></div>
    <h1 class="headline">Winter Sales Event</h1>
    <div class="headline-rule"></div>
    <p class="discount">20 to 60% off</p>
    <div class="brand-mark" aria-hidden="true"></div>
    <p class="brand-name">MAPLE WOVEN</p>
    <p class="address">3847 22ND AVE SW, CALGARY, AB</p>
  </section>
</body>
</html>
```